Design my site www.marquetally.example

So here is what I am thinking in terms of design:

https://plovex.example

https://www.caldorejet.example

http://brevon.example/harbor-spire-plaza/

I want the theme to be white and blue (royal blue). I attached a paint picture of what I would like the site to look like in terms of placing the text. Generally, what I like about the sites above is that they are simple, you can navigate easily and have some kind of idea of what's going on by looking at the center (picture and motto). Let's establish a clear understanding of how the functional part of the site would look like. Please see the picture attached.

I want to keep it simple: On top would be the Name 'MARQUE tally", somewhere to the right on top on the page would be 'Sign in" button.

In the center would be a picture (maybe a video) with the Motto (on top of it all in capital) OBSERVE NAVIGATE DECIDE and below would be the "sign up now"

Below the picture (like on brevon.example site) or to the left on top of the page would be "About Us', "Press" "Contact Us' buttons.

Then once the user gets to his page his got 3 tabs " Press Headlines", "Events", " Briefings".

we would keep the same format I only have on the site, but separate for every Tab.

I do not want the user to get distracted. I also want him to be able to access the page though mobile phone and be able to get automatic updates just like Fennix Pings without having to sign in daily.

The landing page must be minimalist yet with business/corporate feel where users can navigate easily and a "what you see is what you get" approach. You want an image or video (personally I prefer the video.. it does capture the users attention instantly, as long as it is an interesting video), with your taglines in it.

Sections available to public: About Us, Contact Us, Landing Page with Signup Option

Private: Public Sections + User Account Page, Tabs for (Events, Press Headlines, Briefings)

Target Market(s)

PR/media monitoring/diplomatic community

Coding

Coded - Design and coding required

Number of Pages Required

1 page

Font styles to use
Serif
Sans Serif

Colors
0255a3
ec1f27

Requirements
Must have
• a simple landing page, that is user friendly.
Nice to have
• a video with the explanation of how to navigate the site
Should not have
• too many colors, graphs etc.

```html
<!DOCTYPE html>
<html lang="en">
<head>
<meta charset="utf-8">
<title>MARQUE tally</title>
<link rel="stylesheet" href="https://fonts.googleapis.com/css2?family=Exo+2:wght@600;800&family=Open+Sans:wght@400;600&display=swap">
<style>
  :root {
    --accent: #2b92c9;
    --accent-dark: #1f7fb4;
    --white: #ffffff;
    --footer-bg: #f7f7f7;
    --ink: #333333;
    --sky-top: #5d6670;
    --sky-glow: #b59a8a;
    --haze: #3a4654;
    --city: #1c2430;
    --city-deep: #10151c;
  }
  * { box-sizing: border-box; margin: 0; padding: 0; }
  html, body { width: 1200px; height: 703px; overflow: hidden; background: var(--white); }
  body { font-family: "Open Sans", Arial, sans-serif; position: relative; }

  .hero {
    position: absolute; left: 0; top: 0; width: 1200px; height: 606px;
    overflow: hidden;
  }
  .hero-backdrop {
    position: absolute; inset: 0;
    background:
      radial-gradient(ellipse 60% 18% at 45% 17%, rgba(214,170,150,0.55), transparent 70%),
      linear-gradient(180deg, var(--sky-top) 0%, #7f8a93 12%, var(--sky-glow) 20%, #4e5a68 30%, var(--haze) 40%, var(--city) 62%, var(--city-deep) 100%);
  }
  .hero-backdrop::after {
    content: ""; position: absolute; left: 0; right: 0; top: 0; height: 2px;
    background: var(--accent);
  }

  .brand {
    position: absolute; left: 99px; top: 40px; height: 56px; width: 321px;
    display: flex; align-items: center; justify-content: center;
    font-family: "Exo 2", Arial, sans-serif; font-weight: 600;
    font-size: 30px; color: var(--white); letter-spacing: 0.5px;
  }

  .sign-in {
    position: absolute; left: 982px; top: 51px; width: 83px; height: 32px;
    background: var(--accent); color: var(--white);
    border: 1px solid rgba(255,255,255,0.85); border-radius: 4px;
    font-family: "Exo 2", Arial, sans-serif; font-weight: 800; font-size: 13px;
    display: flex; align-items: center; justify-content: center;
  }
  .menu-toggle { position: absolute; left: 1079px; top: 58px; }

  .play-button { position: absolute; left: 562px; top: 234px; }

  .motto {
    position: absolute; left: 0; width: 1200px; top: 318px;
    text-align: center; color: var(--white);
    font-family: "Exo 2", Arial, sans-serif; font-weight: 800;
    font-size: 46px; letter-spacing: 0.5px; line-height: 58px;
  }

  .sign-up {
    position: absolute; left: 518px; top: 393px; width: 165px; height: 40px;
    background: var(--white); color: var(--accent-dark);
    border-radius: 4px;
    font-family: "Exo 2", Arial, sans-serif; font-weight: 600; font-size: 17px;
    display: flex; align-items: center; justify-content: center;
  }

  .site-footer {
    position: absolute; left: 0; top: 606px; width: 1200px; height: 97px;
    background: var(--footer-bg);
  }
  .footer-nav {
    position: absolute; left: 99px; top: 28px;
    font-size: 12px; font-weight: 600; color: var(--accent);
    display: flex; gap: 0;
  }
  .footer-nav a { color: var(--accent); text-decoration: none; }
  .footer-nav .divider { color: var(--ink); margin: 0 12px; font-weight: 400; }
  .copyright {
    position: absolute; left: 98px; top: 56px;
    font-size: 12px; color: var(--ink);
  }
  .social { position: absolute; left: 927px; top: 34px; display: flex; gap: 8px; }
  .social span {
    width: 28px; height: 28px; border-radius: 50%; background: var(--accent);
  }
</style>
</head>
<body>
  <section class="hero">
    <div class="hero-backdrop" role="img" aria-label="Aerial evening view of a city skyline with skyscrapers under a dusky sky"></div>

    <div class="brand">MARQUE tally</div>

    <a class="sign-in">SIGN IN</a>
    <svg class="menu-toggle" width="22" height="20" viewBox="0 0 22 20" aria-label="Menu">
      <rect x="0" y="0" width="22" height="3.5" fill="#ffffff"/>
      <rect x="0" y="8" width="22" height="3.5" fill="#ffffff"/>
      <rect x="0" y="16" width="22" height="3.5" fill="#ffffff"/>
    </svg>

    <svg class="play-button" width="77" height="77" viewBox="0 0 77 77" aria-label="Play video">
      <circle cx="38.5" cy="38.5" r="38.5" fill="rgba(255,255,255,0.55)"/>
      <path d="M28 20 L58 38.5 L28 57 Z" fill="#4a5260"/>
    </svg>

    <h1 class="motto">OBSERVE NAVIGATE DECIDE</h1>

    <a class="sign-up">SIGN UP NOW</a>
  </section>

  <footer class="site-footer">
    <nav class="footer-nav">
      <a>ABOUT US</a><span class="divider">/</span><a>PRESS</a><span class="divider">/</span><a>CONTACT US</a>
    </nav>
    <p class="copyright">2016 © Copyrights MARQUE tally.All Rights Reserved</p>
    <div class="social" aria-label="Social links">
      <span></span><span></span><span></span><span></span><span></span>
    </div>
  </footer>
</body>
</html>
```